Business Card Design Project

A new design for our business cards for a small casting/talent agency, we would like to incorporate the logo and brand colors within the design, below are the information that should be on the card

(Name)
(Title)

Corvane Reels FZ-LLC
Harlow Studio Park
Building 7, Suite 418
Dubai, UAE
PO Box 681247
+97143810579
info@CorvaneReels.com

Target Market(s)

production companies, film makers, media, entertainment industry

Industry/Entity Type

Business

Requirements
Must have
• logo, logo colors
Nice to have
• cutting edge design, sleek and modern
Should not have
• playful, funky, congested

```html
<!DOCTYPE html>
<html lang="en">
<head>
<meta charset="utf-8">
<title>Corvane Reels — Business Card</title>
<link rel="stylesheet" href="https://fonts.googleapis.com/css2?family=Mulish:wght@400;600;800&display=swap">
<style>
  :root {
    --navy: #1f2f66;
    --ink: #2a2d3a;
    --grey-text: #5d6170;
    --shadow-grey: #d3d6db;
    --band-grey: #b9bec7;
    --paper: #ffffff;
    --backdrop: #e9eaed;
  }
  * { box-sizing: border-box; margin: 0; padding: 0; }
  html, body {
    width: 1200px; height: 900px; overflow: hidden;
    background: var(--backdrop);
    font-family: "Mulish", sans-serif;
    color: var(--ink);
  }
  .sheet {
    position: relative; width: 1200px; height: 900px;
    display: flex; flex-direction: column; align-items: center;
    justify-content: center; gap: 50px;
  }
  .card {
    position: relative; width: 700px; height: 400px;
    background: var(--paper); overflow: hidden;
    box-shadow: 0 6px 18px rgba(20, 24, 40, 0.12);
  }

  /* Front */
  .card__band {
    position: absolute; top: 0; left: 0; right: 0; height: 10px;
    background: var(--navy);
  }
  .card__band-accent {
    position: absolute; top: 10px; left: 0; width: 230px; height: 14px;
    background: var(--band-grey);
  }
  .holder { position: absolute; top: 58px; left: 44px; }
  .holder__name {
    font-weight: 800; font-size: 40px; color: var(--navy);
    letter-spacing: 0.5px; line-height: 1.1;
  }
  .holder__title { font-size: 15px; color: var(--grey-text); margin-top: 4px; }

  .contact {
    position: absolute; top: 190px; left: 44px;
    font-size: 17px; line-height: 1.45; color: var(--grey-text);
  }
  .contact__company { font-weight: 800; color: var(--navy); }
  .contact__line { display: flex; align-items: center; gap: 9px; }
  .contact__icon { width: 13px; height: 13px; flex: none; }

  .silhouette-art {
    position: absolute; right: 0; bottom: 0; width: 330px; height: 250px;
    background: radial-gradient(ellipse at 70% 75%, var(--shadow-grey) 0%, var(--shadow-grey) 55%, rgba(211,214,219,0) 75%);
  }

  /* Back */
  .brand {
    position: absolute; top: 50%; left: 130px; transform: translateY(-50%);
    display: flex; align-items: center; gap: 22px;
  }
  .brand__dot { width: 150px; height: 150px; border-radius: 50%; background: var(--navy); }
  .brand__name { font-weight: 800; font-size: 40px; color: var(--navy); }
  .site {
    position: absolute; right: 40px; bottom: 36px;
    font-size: 15px; font-weight: 600; color: var(--ink);
  }
</style>
</head>
<body>
<main class="sheet">

  <section class="card card--front">
    <div class="card__band"></div>
    <div class="card__band-accent"></div>

    <header class="holder">
      <h1 class="holder__name">Dana Whitlock</h1>
      <p class="holder__title">President &amp; CEO</p>
    </header>

    <address class="contact" style="font-style:normal">
      <p class="contact__company">Corvane Reels FZ-LLC</p>
      <p>Harlow Studio Park, Building 7, Suite 418</p>
      <p>Dubai, UAE, PO Box 681247</p>
      <p class="contact__line">
        <svg class="contact__icon" viewBox="0 0 14 14" aria-hidden="true">
          <rect width="14" height="14" rx="2" fill="#1f2f66"/>
          <path d="M4 3.2h1.8l.8 2-1 .8a6 6 0 0 0 2.4 2.4l.8-1 2 .8V10a1 1 0 0 1-1 1A7 7 0 0 1 3 4.2a1 1 0 0 1 1-1z" fill="#fff"/>
        </svg>
        +97143810579
      </p>
      <p class="contact__line">
        <svg class="contact__icon" viewBox="0 0 14 14" aria-hidden="true">
          <rect width="14" height="14" rx="2" fill="#1f2f66"/>
          <rect x="3" y="4" width="8" height="6" fill="#fff"/>
          <path d="M3 4l4 3.2L11 4" fill="none" stroke="#1f2f66" stroke-width="1"/>
        </svg>
        info@CorvaneReels.com
      </p>
    </address>

    <div class="silhouette-art" role="img" aria-label="Soft grey shadow-puppet illustration of hands and a figure"></div>
  </section>

  <section class="card card--back">
    <div class="brand">
      <span class="brand__dot" aria-hidden="true"></span>
      <span class="brand__name">Corvane Reels</span>
    </div>
    <p class="site">www.CorvaneReels.com</p>
  </section>

</main>
</body>
</html>
```